harbor lantern security & electric needs a business card

Must be attractive and modern, look professional and upscale!!
We provide alarm and cameras services and 24 hour monitoring for commercial and residential clients. In addition, the owner is a master electrician that provides services to commercial and residential clients.
We also install and service automatic gates. We previously had two different businesses but decided to merge into one, thus creating Harbor Lantern Security & Electric.

Target Market(s)

Commercial Business and residential customers

Industry/Entity Type

Security

Contact Information for Business Card

Front and back design with logo and services listed

Font styles to use
Sans Serif

Colors
ec1f27
0355a3
fbee3f

Requirements
Must have
• Front of card:
• Marcus Tremblow-Owner
• telephone icon and then the number 555-555-0193
• Mail icon and then email address mtremblow@quillmail.example
• World Icon then website www.yourharborlanterntx.example
• Location marker and then Lanternport, Coastland
• We would like to have a picture of the logo at least on the front
• Also need motto on front: We're There When You're Not
• The front of the card must also say Licensed and Insured in addition to:
• License Number: K47315
• TECL: 58629
• On the Back of the Card:
• List each of these Services with check marks:
• Residential and Commercial Electrical Services
• Electric Gates
• Alarm Systems
• Alarm Monitoring
• Cameras
• ***Use separate attached logo, the business card design is just to be used as a model***
Nice to have
• It would be nice to have the logo on back of the card in addition to these words at the bottom:
• "No job too big or small, we do it all!"
Should not have
• Anything crazy!!

```html
<!DOCTYPE html>
<html lang="en">
<head>
<meta charset="utf-8">
<title>Harbor Lantern Security &amp; Electric — Business Card</title>
<link rel="stylesheet" href="https://fonts.googleapis.com/css2?family=Montserrat:wght@400;500;600;700;800&display=swap">
<style>
  :root {
    --card-blue: #2c4380;
    --card-blue-deep: #253a72;
    --accent-red: #e8232c;
    --ink-white: #ffffff;
    --ink-soft: rgba(255,255,255,0.55);
    --stage: #e9ebf0;
  }
  * { box-sizing: border-box; margin: 0; padding: 0; }
  html, body { width: 1200px; height: 900px; overflow: hidden; }
  body {
    background: var(--stage);
    font-family: "Montserrat", Arial, sans-serif;
    color: var(--ink-white);
    position: relative;
  }
  .card {
    position: absolute;
    left: 250px;
    width: 700px;
    height: 400px;
    background: var(--card-blue);
    box-shadow: 0 12px 30px rgba(20,30,60,0.25);
    overflow: hidden;
  }
  .card--back { top: 30px; background: linear-gradient(135deg, #34508f 0%, var(--card-blue) 55%, var(--card-blue-deep) 100%); }
  .card--front { top: 470px; }

  .rule { position: absolute; height: 1.5px; background: var(--accent-red); }
  .divider {
    position: absolute; width: 1.5px;
    background: linear-gradient(to bottom, transparent, var(--ink-soft), transparent);
  }

  .brand-square { width: 16px; height: 16px; background: var(--accent-red); flex: none; }
  .brand-name { font-weight: 800; line-height: 1.2; color: var(--ink-white); }

  /* back */
  .back-brand {
    position: absolute; left: 32px; top: 158px; width: 190px;
    display: flex; align-items: center; gap: 10px;
  }
  .back-brand .brand-name { font-size: 16px; }
  .card--back .divider { left: 240px; top: 110px; height: 180px; }
  .services { position: absolute; left: 264px; top: 124px; list-style: none; }
  .services li {
    display: flex; align-items: center; gap: 10px;
    font-weight: 700; font-size: 14px; line-height: 1.85; white-space: nowrap;
  }
  .services svg { width: 13px; height: 13px; flex: none; }
  .back-tagline {
    position: absolute; left: 0; right: 0; bottom: 30px;
    text-align: center; font-weight: 700; font-size: 19px; letter-spacing: 0.3px;
  }

  /* front */
  .front-brand { position: absolute; left: 40px; top: 140px; width: 260px; }
  .front-brand .brand-row { display: flex; align-items: center; gap: 12px; }
  .front-brand .brand-name { font-size: 21px; }
  .motto {
    margin-top: 12px; padding-top: 8px;
    border-top: 1.5px solid var(--accent-red);
    font-weight: 600; font-size: 12px; letter-spacing: 0.6px; text-transform: uppercase;
  }
  .card--front .divider { left: 325px; top: 90px; height: 180px; }
  .contact { position: absolute; left: 355px; top: 100px; }
  .contact-name { font-weight: 800; font-size: 24px; letter-spacing: 0.3px; }
  .contact-role { font-weight: 700; font-size: 17px; color: var(--accent-red); margin-bottom: 8px; }
  .contact-list { list-style: none; }
  .contact-list li {
    display: flex; align-items: center; gap: 10px;
    font-weight: 600; font-size: 15px; line-height: 1.7; white-space: nowrap;
  }
  .contact-list svg { width: 14px; height: 14px; flex: none; }
  .url-highlight { color: var(--accent-red); }
  .credentials {
    position: absolute; left: 0; right: 0; bottom: 32px;
    text-align: center; font-weight: 700; font-size: 18px;
  }
  .credentials .dot {
    display: inline-block; width: 9px; height: 9px; border-radius: 50%;
    background: var(--accent-red); margin: 0 8px; vertical-align: middle;
  }
</style>
</head>
<body>

<section class="card card--back" aria-label="Card back">
  <div class="rule" style="right:0; top:78px; width:130px;"></div>
  <div class="back-brand">
    <span class="brand-square"></span>
    <span class="brand-name">Harbor Lantern Security &amp; Electric</span>
  </div>
  <div class="divider"></div>
  <ul class="services">
    <li><svg viewBox="0 0 14 14"><path d="M1 7.5 5 11.5 13 2.5" fill="none" stroke="#e8232c" stroke-width="2.6" stroke-linecap="round" stroke-linejoin="round"/></svg><span>Residential &amp; Commercial Electrical Services</span></li>
    <li><svg viewBox="0 0 14 14"><path d="M1 7.5 5 11.5 13 2.5" fill="none" stroke="#e8232c" stroke-width="2.6" stroke-linecap="round" stroke-linejoin="round"/></svg><span>Electric Gates</span></li>
    <li><svg viewBox="0 0 14 14"><path d="M1 7.5 5 11.5 13 2.5" fill="none" stroke="#e8232c" stroke-width="2.6" stroke-linecap="round" stroke-linejoin="round"/></svg><span>Alarm Systems</span></li>
    <li><svg viewBox="0 0 14 14"><path d="M1 7.5 5 11.5 13 2.5" fill="none" stroke="#e8232c" stroke-width="2.6" stroke-linecap="round" stroke-linejoin="round"/></svg><span>Alarm Monitoring</span></li>
    <li><svg viewBox="0 0 14 14"><path d="M1 7.5 5 11.5 13 2.5" fill="none" stroke="#e8232c" stroke-width="2.6" stroke-linecap="round" stroke-linejoin="round"/></svg><span>Cameras</span></li>
  </ul>
  <div class="rule" style="left:0; bottom:42px; width:150px;"></div>
  <p class="back-tagline">No job too big or small, we do it all</p>
</section>

<section class="card card--front" aria-label="Card front">
  <div class="front-brand">
    <div class="brand-row">
      <span class="brand-square"></span>
      <span class="brand-name">Harbor Lantern Security &amp; Electric</span>
    </div>
    <p class="motto">We're There When You're Not</p>
  </div>
  <div class="divider"></div>
  <div class="contact">
    <p class="contact-name">Marcus Tremblow</p>
    <p class="contact-role">Owner</p>
    <ul class="contact-list">
      <li><svg viewBox="0 0 14 14"><path d="M3 1h2.5l1 3-1.6 1.2a8 8 0 0 0 3.9 3.9L10 7.5l3 1V11a2 2 0 0 1-2 2A10 10 0 0 1 1 3a2 2 0 0 1 2-2z" fill="#e8232c"/></svg><span>555-555-0193</span></li>
      <li><svg viewBox="0 0 14 14"><rect x="1" y="3" width="12" height="8.5" rx="1" fill="none" stroke="#e8232c" stroke-width="1.6"/><path d="M1.5 3.5 7 8l5.5-4.5" fill="none" stroke="#e8232c" stroke-width="1.6"/></svg><span>mtremblow@quillmail.example</span></li>
      <li><svg viewBox="0 0 14 14"><circle cx="7" cy="7" r="5.8" fill="none" stroke="#e8232c" stroke-width="1.4"/><ellipse cx="7" cy="7" rx="2.6" ry="5.8" fill="none" stroke="#e8232c" stroke-width="1.2"/><path d="M1.2 7h11.6" stroke="#e8232c" stroke-width="1.2"/></svg><span>www.<span class="url-highlight">yourharborlanterntx</span>.example</span></li>
      <li><svg viewBox="0 0 14 14"><path d="M7 13.5S2.2 8.4 2.2 5.3a4.8 4.8 0 0 1 9.6 0C11.8 8.4 7 13.5 7 13.5z" fill="#e8232c"/><circle cx="7" cy="5.3" r="1.8" fill="#2c4380"/></svg><span>Lanternport, Coastland</span></li>
    </ul>
  </div>
  <div class="rule" style="right:0; top:40px; width:70px;"></div>
  <div class="rule" style="left:0; bottom:44px; width:60px;"></div>
  <p class="credentials">Licensed and Insured<span class="dot"></span>License Number: K47315, TECL: 58629</p>
</section>

</body>
</html>
```